Stationary ("email stationary") and business card for a unique soccer training program
Video analysis of players technique
Use specific fonts
use Impact and/or Eurostar Black Extended
Professional
Ode Tralmo
owner
P.O. Box 738 Commack, NY 11592
boltpassdrill@mailvane.net
www.boltpassdrill.net
the logo include the company name and tag line...it must be featured prominently on the business card
- Video based analysis of players' technique of soccer fundementals - specializing in repairing shooting mechanics - Clear and easy footprint to future success Date: _____ Time: ____ Location: _______

```html
<!DOCTYPE html>
<html lang="en">
<head>
<meta charset="utf-8">
<title>Bolt Pass Drill — Stationery Set</title>
<link href="https://fonts.googleapis.com/css2?family=Anton&family=Michroma&family=Roboto:wght@400;700&display=swap" rel="stylesheet">
<style>
  :root{
    --bg:#ececec;
    --paper:#ffffff;
    --ink:#0c0c0c;
    --red:#d8121b;
    --text-soft:#cfcfcf;
    --text-grey:#6d6d6d;
  }
  *{box-sizing:border-box;margin:0;padding:0}
  html,body{width:1200px;height:936px;overflow:hidden;background:var(--bg)}
  body{position:relative;font-family:"Roboto",Arial,sans-serif}
  .piece{position:absolute;background:var(--paper);overflow:hidden}
  .piece svg.art{position:absolute;left:0;top:0;width:100%;height:100%}
  .brand{position:absolute;display:flex;align-items:center;gap:6px;font-family:"Anton",Impact,sans-serif;color:#fff;text-transform:uppercase;letter-spacing:.5px;white-space:nowrap}
  .brand .dot{border-radius:50%;background:#fff;flex:none}
  .contact{position:absolute;font-size:6px;line-height:9px;color:var(--text-soft);list-style:none;white-space:nowrap}
  .contact li{display:flex;align-items:center;gap:4px}
  .contact li::before{content:"";width:4px;height:4px;background:var(--red);border-radius:1px;flex:none}
  .url{position:absolute;font-family:"Michroma",sans-serif;color:var(--text-grey);letter-spacing:2px;white-space:nowrap}

  .letterhead{left:180px;top:41px;width:386px;height:517px}
  .letterhead .brand{left:14px;top:22px;font-size:13px}
  .letterhead .brand .dot{width:14px;height:14px}
  .letterhead .contact{left:300px;top:16px}

  .folder{left:634px;top:41px;width:426px;height:573px;background:var(--ink)}
  .folder .brand{left:0;right:0;top:250px;justify-content:center;font-size:30px;gap:12px}
  .folder .brand .dot{width:34px;height:34px}
  .folder .url{left:0;right:0;bottom:14px;text-align:center;font-size:9px}

  .card-front{left:43px;top:652px;width:180px;height:104px;background:var(--ink)}
  .card-front .brand{left:10px;top:14px;font-size:9px;gap:4px}
  .card-front .brand .dot{width:10px;height:10px}
  .card-front .person{position:absolute;left:100px;top:12px;color:#fff}
  .card-front .person .name{font-family:"Anton",Impact,sans-serif;font-size:8px;color:var(--red);letter-spacing:.3px}
  .card-front .person .role{font-size:5.5px;color:var(--text-soft)}
  .card-front .contact{left:100px;top:36px;font-size:4.6px;line-height:7px}
  .card-front .contact li::before{width:3px;height:3px}

  .card-back{left:43px;top:769px;width:180px;height:107px}
  .card-back .services{position:absolute;left:10px;top:10px;width:160px;font-size:4.8px;line-height:7px;color:#fff;list-style:none}

  .compliment{left:241px;top:670px;width:358px;height:205px}
  .compliment .brand{left:14px;top:12px;font-size:11px}
  .compliment .brand .dot{width:12px;height:12px}
  .compliment .contact{left:262px;top:10px;font-size:5.2px;line-height:8px}

  .envelope{left:665px;top:670px;width:467px;height:205px}
  .envelope .url{right:18px;top:12px;font-size:9px}
</style>
</head>
<body>

<section class="piece letterhead" aria-label="Letterhead">
  <svg class="art" viewBox="0 0 386 517" preserveAspectRatio="none" aria-hidden="true">
    <defs>
      <linearGradient id="lhSilver" x1="0" y1="0" x2="1" y2="0">
        <stop offset="0" stop-color="#f2f2f2"/><stop offset=".5" stop-color="#a9a9a9"/><stop offset="1" stop-color="#e8e8e8"/>
      </linearGradient>
    </defs>
    <path d="M0 0H386V80C280 62 140 66 0 104Z" fill="url(#lhSilver)"/>
    <path d="M0 0H386V66C270 52 130 58 0 90Z" fill="#0c0c0c"/>
  </svg>
  <div class="brand"><span class="dot"></span>Bolt Pass Drill</div>
  <ul class="contact">
    <li>P.O. Box 738</li>
    <li>Varnell, NY 11592</li>
    <li>Ode Tralmo</li>
    <li>boltpassdrill@mailvane.net</li>
    <li>www.boltpassdrill.net</li>
  </ul>
</section>

<section class="piece folder" aria-label="Presentation folder">
  <svg class="art" viewBox="0 0 426 573" preserveAspectRatio="none" aria-hidden="true">
    <defs>
      <linearGradient id="fdSilver" x1="0" y1="0" x2="1" y2="0">
        <stop offset="0" stop-color="#9a9a9a"/><stop offset=".45" stop-color="#f0f0f0"/><stop offset="1" stop-color="#a5a5a5"/>
      </linearGradient>
    </defs>
    <path d="M0 520C130 470 290 466 426 486V573H0Z" fill="#d8121b"/>
    <path d="M0 528C140 484 300 482 426 498V573H0Z" fill="url(#fdSilver)"/>
    <path d="M0 552C140 528 300 530 426 540V573H0Z" fill="#ffffff"/>
  </svg>
  <div class="brand"><span class="dot"></span>Bolt Pass Drill</div>
  <div class="url">www.boltpassdrill.net</div>
</section>

<section class="piece card-front" aria-label="Business card front">
  <svg class="art" viewBox="0 0 180 104" preserveAspectRatio="none" aria-hidden="true">
    <defs>
      <linearGradient id="bcSilver" x1="0" y1="0" x2="1" y2="0">
        <stop offset="0" stop-color="#9a9a9a"/><stop offset=".5" stop-color="#eeeeee"/><stop offset="1" stop-color="#a0a0a0"/>
      </linearGradient>
    </defs>
    <path d="M0 92C60 82 120 82 180 88V104H0Z" fill="url(#bcSilver)"/>
  </svg>
  <div class="brand"><span class="dot"></span>Bolt Pass Drill</div>
  <div class="person"><div class="name">Ode Tralmo</div><div class="role">Owner</div></div>
  <ul class="contact">
    <li>P.O. Box 738 Varnell, NY 11592</li>
    <li>boltpassdrill@mailvane.net</li>
    <li>www.boltpassdrill.net</li>
  </ul>
</section>

<section class="piece card-back" aria-label="Business card back">
  <svg class="art" viewBox="0 0 180 107" preserveAspectRatio="none" aria-hidden="true">
    <defs>
      <linearGradient id="cbSilver" x1="0" y1="0" x2="1" y2="0">
        <stop offset="0" stop-color="#f0f0f0"/><stop offset=".5" stop-color="#aaaaaa"/><stop offset="1" stop-color="#e6e6e6"/>
      </linearGradient>
    </defs>
    <path d="M0 0H180V40C120 34 60 38 0 50Z" fill="url(#cbSilver)"/>
    <path d="M0 0H180V34C120 28 60 32 0 44Z" fill="#0c0c0c"/>
  </svg>
  <ul class="services">
    <li>Video based analysis of players' technique</li>
    <li>Specializing in repairing shooting mechanics</li>
    <li>Clear and easy footprint to future success</li>
  </ul>
</section>

<section class="piece compliment" aria-label="Compliment slip">
  <svg class="art" viewBox="0 0 358 205" preserveAspectRatio="none" aria-hidden="true">
    <defs>
      <linearGradient id="csSilver" x1="0" y1="0" x2="1" y2="0">
        <stop offset="0" stop-color="#f2f2f2"/><stop offset=".5" stop-color="#a9a9a9"/><stop offset="1" stop-color="#e8e8e8"/>
      </linearGradient>
    </defs>
    <path d="M0 0H358V62C250 50 130 54 0 80Z" fill="url(#csSilver)"/>
    <path d="M0 0H358V50C250 40 130 44 0 66Z" fill="#0c0c0c"/>
  </svg>
  <div class="brand"><span class="dot"></span>Bolt Pass Drill</div>
  <ul class="contact">
    <li>P.O. Box 738</li>
    <li>Varnell, NY 11592</li>
    <li>boltpassdrill@mailvane.net</li>
    <li>www.boltpassdrill.net</li>
  </ul>
</section>

<section class="piece envelope" aria-label="Envelope">
  <svg class="art" viewBox="0 0 467 205" preserveAspectRatio="none" aria-hidden="true">
    <defs>
      <linearGradient id="evSilver" x1="0" y1="0" x2="1" y2="0">
        <stop offset="0" stop-color="#f2f2f2"/><stop offset=".5" stop-color="#a3a3a3"/><stop offset="1" stop-color="#e4e4e4"/>
      </linearGradient>
    </defs>
    <path d="M0 0H467V34C320 26 160 34 0 64Z" fill="url(#evSilver)"/>
  </svg>
  <div class="url">www.boltpassdrill.net</div>
</section>

</body>
</html>
```